Affiliate website design and wireframe

We need a design of an affiliate website for an application we purchased, it is important that you build the website pages according to the developer of the applications specifications (please see attached documents) the developer of the application will configure the pages and add them to the site. Please take special note of his comments below.

We all so need you to create a wire frame so the developer can test everything (http://sketchwire.tolvaro.vn/)

It will be the homepage and about 16 inner pages (please see attached files)
Here is our website http://bluvendmarket.com/affiliate/affiliates/index.php

The version of the software we purchased is the Kivo Partner Hubline version

Comments from the developers

1. I will need the source files of the design (photoshop .psd files and font files if custom fonts are used), since the implementation is closely bound to component sizes (like border width, margin width etc.) and colors. If you own a corporate design manual, it's crucial to send it as well. Also, please, make sure if you use custom fonts, that these allow legal website integration (like google web fonts).

2. Any and every content is controlled via templates. All editing/adding/removing etc. is done here. The template files are essentially html/php documents, they use a template engine called quillo (http://www.quillo.net/) which has it's own language similar to php.

3. .psd files are ideal, because we deal with the specifics of KPX/KPH implementation on a daily basis. Any html/css developed in advance may prove to be a poor choice. You may choose to let an in-house developer do the job, but experience wise this is more costly, since he will not be accustomed to the template/functionality systems of KPX/KPH.

4. I will need the source files of the design (photoshop .psd files and font files if custom fonts are used), since the implementation is closely bound to component sizes (like border width, margin width etc.) and colors. If you own a corporate design manual, it's crucial to send it as well. Also, please, make sure if you use custom fonts, that these allow legal website integration (like google web fonts).

Regards,

Dorek Hanval
Multimedia Design

We prefer illustrations more than pictures of real people.

This is the home page, it is asking for Merchant and Affiliate sign up, not just affiliate.

http://bluvendmarket.com/affiliate/index.php

Please note the home page features both Merchant and Affiliate sign up

We are looking for illustration design not just stock images

Please remember the search menu that searches for the available programs, see the example we gave you, look at the search menu at the top of the page http://www.tradelumo.com/

We are reviewing everything, no need to send more designs

Target Market(s)

Natural Products Manufacturers
Natural products Sales reps
Natural Products Bloggers
Social Marketing

Industry/Entity Type

Software

Requirements
Must have
• 1. All links on pages should go to the appropriate pages.
2. Colors can be based on our logo design (look at the attachments)
3. Here is our website http://bluvendmarket.com/affiliate/affiliates/index.php
4. We have attached a drawing of how we think the homepage concept should follow.
5. Main concept of design, is trying to show our sales people (Affiliates) are doing multiple things to advertise and sell the merchants products.(see logo)
6. Need to be able to edit all text and images.
7. Our target audience is Natural product sales people (Advertisers, bloggers, ext) and natural product manufacturers.
8. You can speak to the company who made the application, through live chat, on there website http://www.kivopartnerhubline.com/
Nice to have
• See Attached Documents.
site should take up whole website pages
Look For fun Illustrated Website, one of the better ones we have seen is http://www.tradelumo.com/index.cfm
Should not have
• Please look very carefully at developers comment above.

```html
<!DOCTYPE html>
<html lang="en">
<head>
<meta charset="utf-8">
<title>BluvendMarket.com – Affiliate Program</title>
<link rel="stylesheet" href="https://fonts.googleapis.com/css2?family=Roboto+Condensed:wght@400;700&family=Roboto:wght@300;400;500;700&display=swap">
<style>
:root{
  --navy:#1c3557;
  --navy-btn:#1e4a75;
  --blue-title:#1d4f7a;
  --step-blue:#2f5b83;
  --green:#5aa51e;
  --lime:#9ab92a;
  --hero-bg:#f0f0f0;
  --feature-bg:#f7f7f7;
  --dark:#2b2f33;
  --footer:#1b2b3c;
  --footer-bottom:#15222f;
  --text:#222;
  --muted:#8a8a8a;
  --social:#2a9ad7;
  --store-blue:#1a87d8;
  --store-orange:#f0773a;
}
*{margin:0;padding:0;box-sizing:border-box}
html,body{width:723px;height:1200px;overflow:hidden}
body{position:relative;font-family:"Roboto",Arial,sans-serif;color:var(--text);background:#fff}
.abs{position:absolute}

/* top bar */
.topbar{left:0;top:0;width:723px;height:22px;background:var(--navy);color:#fff;font-size:7px;font-weight:500}
.topbar .welcome{left:79px;top:7px}
.topbar .link{top:7px;display:flex;align-items:center;gap:4px}
.topbar .aff{left:395px}
.topbar .mer{left:472px}
.search{left:545px;top:3px;width:88px;height:16px;background:#eef1f4;border:1px solid #cfd6de}
.search-btn{left:632px;top:3px;width:16px;height:16px;background:#142a45}

/* header */
.header{left:0;top:22px;width:723px;height:47px;background:#fff;box-shadow:0 1px 2px rgba(0,0,0,.08);z-index:2}
.brand{left:77px;top:9px;font-family:"Roboto Condensed",sans-serif;font-weight:700;font-size:25px;letter-spacing:-.5px;color:var(--green);text-transform:uppercase}
.nav{top:17px;font-size:10.5px;color:var(--navy)}
.nav.home{left:509px;color:var(--green)}
.nav.signup{left:551px}
.nav.contact{left:601px}
.nav-active{left:501px;top:45px;width:41px;height:2px;background:var(--green)}

/* hero */
.hero{left:0;top:69px;width:723px;height:270px;background:linear-gradient(180deg,#f6f6f6,var(--hero-bg))}
.hero-scene{left:0;top:60px;width:360px;height:210px;background:linear-gradient(180deg,rgba(255,255,255,0),rgba(215,215,215,.55))}
.hero-title{left:80px;top:82px;font-family:"Roboto Condensed",sans-serif;font-weight:700;font-size:21px;color:var(--text)}
.hero-text{left:81px;top:110px;width:270px;font-size:8px;line-height:10px;color:#333}
.btn{display:flex;align-items:center;justify-content:center;color:#fff;font-family:"Roboto Condensed",sans-serif;font-weight:700;font-size:8.5px;text-transform:uppercase}
.btn-signup{left:81px;top:145px;width:91px;height:26px;background:var(--navy-btn)}
.btn-login{left:178px;top:145px;width:92px;height:26px;background:var(--green)}
.hero-illustration{left:365px;top:31px;width:277px;height:239px;background:radial-gradient(ellipse at 55% 65%,#24466f 0%,#3d6e9e 35%,rgba(160,200,90,.35) 60%,rgba(230,230,230,0) 78%)}

/* features */
.features{left:0;top:339px;width:723px;height:206px;background:var(--feature-bg)}
.feature{top:0;width:200px;height:206px;text-align:center}
.feature .icon{display:block;margin:24px auto 0}
.feature h3{margin-top:14px;font-size:10px;font-weight:400;line-height:12px;color:var(--blue-title)}
.feature p{margin:12px auto 0;width:158px;font-size:6.5px;line-height:10px;font-weight:300;color:var(--muted);text-align:justify;text-align-last:center}
.f1{left:60px}.f2{left:261px}.f3{left:461px}
.divider{top:0;width:2px;height:206px;background:#e9e9e9}
.divider.d1{left:264px}.divider.d2{left:462px}
.divider-accent{top:157px;width:3px;height:49px;background:var(--step-blue)}
.divider-accent.d1{left:264px}.divider-accent.d2{left:461px}
.features-rule{left:0;top:545px;width:723px;height:3px;background:var(--step-blue)}

/* how it works */
.how{left:0;top:548px;width:723px;height:330px;background:linear-gradient(160deg,#23272b,var(--dark) 50%,#3a3f45)}
.how-title{left:0;top:572px;width:723px;text-align:center;color:#fff;font-family:"Roboto Condensed",sans-serif;font-weight:700;font-size:18px}
.how-sub{left:110px;top:597px;width:503px;text-align:center;color:#fff;font-size:7px;line-height:9.5px;font-weight:700;text-transform:uppercase}
.step{width:171px;height:93px;background:linear-gradient(180deg,#fff,#ececec);font-size:8px;line-height:10.5px;color:#555;padding:30px 20px 0;text-align:center}
.step.justify{text-align:justify;text-align-last:center}
.num{width:35px;height:35px;border-radius:50%;background:var(--step-blue);color:#fff;font-family:"Roboto Condensed",sans-serif;font-weight:700;font-size:19px;display:flex;align-items:center;justify-content:center}

/* ready to join */
.ready{left:0;top:878px;width:723px;height:144px;background:var(--lime)}
.ready-title{left:0;top:901px;width:723px;text-align:center;font-family:"Roboto Condensed",sans-serif;font-weight:700;font-size:16px;color:#111}
.ready-sub{left:96px;top:927px;width:531px;text-align:center;color:#fff;font-size:7px;line-height:10px;text-transform:uppercase}
.btn-join{left:255px;top:964px;width:214px;height:38px;background:var(--navy-btn);font-size:17px;font-weight:400;font-family:"Roboto Condensed",sans-serif;text-transform:none}

/* footer */
.footer{left:0;top:1022px;width:723px;height:128px;background:var(--footer);color:#fff}
.fcol{top:25px}
.fcol h4{font-size:8.5px;font-weight:400;margin-bottom:9px}
.fcol ul{list-style:none}
.fcol li{font-size:7px;line-height:11.6px;display:flex;align-items:center;gap:3px;color:#e8edf2}
.fcol li::before{content:"";width:5px;height:5px;border:1px solid #e8edf2;border-radius:50%}
.c1{left:82px}.c2{left:223px}.c3{left:377px}.c4{left:501px}
.store{top:52px;width:64px;height:21px;border-radius:2px}
.store.ios{left:501px;background:var(--store-blue)}
.store.play{left:569px;background:var(--store-orange)}

.bottom{left:0;top:1150px;width:723px;height:50px;background:var(--footer-bottom);color:#9aa7b4;font-size:7px}
.copy{left:78px;top:21px;display:flex;gap:9px}
.social{top:11px;width:28px;height:28px;border-radius:50%;background:var(--social)}
.s1{left:558px}.s2{left:587px}.s3{left:616px}
</style>
</head>
<body>

<!-- top bar -->
<div class="abs topbar">
  <span class="abs welcome">Default welcome msg!</span>
  <span class="abs link aff">
    <svg width="8" height="8" viewBox="0 0 8 8"><rect x=".5" y="1.5" width="6" height="6" fill="none" stroke="#fff"/><path d="M3 5l4-4" stroke="#fff"/></svg>
    Affiliate login</span>
  <span class="abs link mer">
    <svg width="7" height="8" viewBox="0 0 7 8"><circle cx="3.5" cy="2" r="2" fill="#fff"/><path d="M0 8a3.5 3.5 0 0 1 7 0z" fill="#fff"/></svg>
    Merchant login</span>
  <div class="abs search"></div>
  <div class="abs search-btn">
    <svg width="16" height="16" viewBox="0 0 16 16"><circle cx="7" cy="7" r="3" fill="none" stroke="#fff" stroke-width="1.3"/><path d="M9.2 9.2l3 3" stroke="#fff" stroke-width="1.5"/></svg>
  </div>
</div>

<!-- header -->
<header class="abs header">
  <div class="abs brand">BluvendMarket.com</div>
  <a class="abs nav home">Home</a>
  <a class="abs nav signup">Sign up</a>
  <a class="abs nav contact">Contact us</a>
  <div class="abs nav-active"></div>
</header>

<!-- hero -->
<section class="abs hero">
  <div class="abs hero-scene" role="img" aria-label="Faint city skyline and clouds"></div>
  <h1 class="abs hero-title">START MAKING MONEY NOW!</h1>
  <p class="abs hero-text">There is no charge to join our Affiliate Program.We pay commissions for all sales you referred.Earn up to 30% commissions</p>
  <a class="abs btn btn-signup">Affiliates signup</a>
  <a class="abs btn btn-login">Login</a>
  <div class="abs hero-illustration" role="img" aria-label="Illustrated affiliate in a suit with raised arms, surrounded by email, text, blog, social and phone icons"></div>
</section>

<!-- features -->
<section class="abs features">
  <div class="abs divider d1"></div>
  <div class="abs divider d2"></div>
  <div class="abs divider-accent d1"></div>
  <div class="abs divider-accent d2"></div>

  <div class="abs feature f1">
    <svg class="icon" width="40" height="40" viewBox="0 0 40 40">
      <circle cx="16" cy="9" r="6" fill="#4a4f55"/>
      <path d="M4 34c0-9 5-15 12-15s10 4 11 8v7z" fill="#4a4f55"/>
      <circle cx="29" cy="29" r="8" fill="#4a4f55" stroke="#f7f7f7" stroke-width="2"/>
      <text x="29" y="33" font-size="11" font-family="Roboto,sans-serif" font-weight="700" fill="#fff" text-anchor="middle">$</text>
    </svg>
    <h3>Earn up to 50% commission for all products!</h3>
    <p>Not only can you join our team and help spread the word about your favorite products, you can get rewarded for your efforts. Our system tracks referrals and pays top commissions for every client you send our way.</p>
  </div>

  <div class="abs feature f2">
    <svg class="icon" width="40" height="40" viewBox="0 0 40 40">
      <circle cx="15" cy="15" r="10" fill="#4a4f55"/>
      <text x="15" y="19.5" font-size="12" font-family="Roboto,sans-serif" font-weight="700" fill="#fff" text-anchor="middle">$</text>
      <circle cx="26" cy="26" r="10" fill="#4a4f55" stroke="#f7f7f7" stroke-width="2"/>
      <text x="26" y="30.5" font-size="12" font-family="Roboto,sans-serif" font-weight="700" fill="#fff" text-anchor="middle">€</text>
    </svg>
    <h3>High Conversion Rate = More<br>Money.</h3>
    <p>Our website and plans generate one of the highest conversion rates in the industry. Our high conversion rates mean that the people who you send here are more likely to buy our products. Of course we can't prove that either, but if you don't trust us, why would you want to refer people here?</p>
  </div>

  <div class="abs feature f3">
    <svg class="icon" width="40" height="40" viewBox="0 0 40 40">
      <path d="M12 8.5A16 16 0 1 0 20 4" fill="none" stroke="#4a4f55" stroke-width="3.5" stroke-linecap="round"/>
      <path d="M20 20l-7-8" stroke="#4a4f55" stroke-width="3.5" stroke-linecap="round"/>
      <circle cx="20" cy="20" r="2.5" fill="#4a4f55"/>
    </svg>
    <h3>Long cookie duration.</h3>
    <p>If a customer comes from your site to ours, and then comes back to purchase six months later, you get credit.</p>
  </div>
</section>
<div class="abs features-rule"></div>

<!-- how it works -->
<section class="abs how" role="img" aria-label="Darkened photo of a desk with charts and documents"></section>
<h2 class="abs how-title">HOW DOES IT WORK?</h2>
<p class="abs how-sub">It couldn't be simpler! We've streamlined our entire affiliate process to ensure ease of use, while still maintaining extremely accurate affiliate tracking. The process is as follows:</p>

<div class="abs step" style="left:82px;top:644px">Visitor clicks on an affiliate link on your site or in an email.</div>
<div class="abs step justify" style="left:277px;top:644px">The visitors IP is logged and a cookie is placed in their browser for tracking purposes.</div>
<div class="abs step" style="left:471px;top:644px">The visitor browses our site, and may decide to order.</div>
<div class="abs step justify" style="left:82px;top:764px">If the visitor orders (the order need not be placed during the same browser session--cookies and IPs are stored indefinitely), the order will be registered as a sale for you</div>
<div class="abs step justify" style="left:277px;top:764px">We will review and approve the sale.</div>
<div class="abs step justify" style="left:471px;top:764px">You will receive commission payouts.</div>

<div class="abs num" style="left:150px;top:626px">1</div>
<div class="abs num" style="left:345px;top:626px">2</div>
<div class="abs num" style="left:540px;top:626px">3</div>
<div class="abs num" style="left:150px;top:746px">4</div>
<div class="abs num" style="left:345px;top:746px">5</div>
<div class="abs num" style="left:540px;top:746px">6</div>

<!-- ready to join -->
<section class="abs ready"></section>
<h2 class="abs ready-title">READY TO JOIN?</h2>
<p class="abs ready-sub">It couldn't be simpler! We've streamlined our entire affiliate process to ensure ease of use, while still maintaining extremely accurate affiliate tracking. The process is as follows:</p>
<a class="abs btn btn-join">JOIN NOW!</a>

<!-- footer -->
<footer class="abs footer">
  <div class="abs fcol c1"><h4>About us</h4><ul><li>Company</li><li>Contact us</li><li>Privacy Policy</li></ul></div>
  <div class="abs fcol c2"><h4>Affiliates</h4><ul><li>Affiliates information</li><li>Affiliate link formats</li></ul></div>
  <div class="abs fcol c3"><h4>Affiliates</h4><ul><li>Merchants Login</li><li>Integration methods</li><li>API Reference</li><li>Samples and Tests</li><li>Relay Partner Suite</li></ul></div>
  <div class="abs fcol c4"><h4>Mobile</h4></div>
  <div class="abs store ios" role="img" aria-label="App store badge"></div>
  <div class="abs store play" role="img" aria-label="Play store badge"></div>
</footer>

<div class="abs bottom">
  <div class="abs copy"><span>© 2014 bluvendmarket.com All rights reserved</span><span>Terms of Service</span><span>Privacy Policy</span></div>
  <div class="abs social s1" role="img" aria-label="Social link"></div>
  <div class="abs social s2" role="img" aria-label="Social link"></div>
  <div class="abs social s3" role="img" aria-label="Social link"></div>
</div>

</body>
</html>
```